Cannabis company needs an e-commerce website

Our retail cannabis company Vale Ember needs a fully functioning e-commerce website optimized for SEO. We want the website to have the appeal and sophistication of a cigar lounge/boutique coffee shop highlighting our high-end artisanal products. It should have the ability to categorize and search for products based on tags. Our initial number of SKUs will be about 25, but that will grow as the business grows.

Target Market(s)

Online retail cannabis users

Industry/Entity Type

Cannabis

Coding

Coded - Design and coding required

Number of Pages Required

5+ page

Font styles to use
Sans Serif

Requirements
Must have
• - Age confirmation (19+) confirmation popup
- Very simple and easy method of purchasing based on different product sizes
- Search functionality based on tags etc. of the products
- Similar functionality to the following websites:
1) https://www.fernbrookherbals.com/
2) https://mossparlor.io/
3) https://lunatrove.org/
4) https://plumcurio.com/
- Similar look to the following websites:
1) https://layoutbazaar.net/item/corvin-pipe-shop-theme/48203917
2) https://www.bramsoil.ca/
3) https://dunmoorguild.org/
4) https://wrenfieldapothecary.com/

```html
<!DOCTYPE html>
<html lang="en">
<head>
<meta charset="utf-8">
<title>Vale Ember – Order Confirmed</title>
<link href="https://fonts.googleapis.com/css2?family=Lato:wght@400;700;900&display=swap" rel="stylesheet">
<style>
:root{
  --bar:#222222;
  --header:#2b2b2b;
  --hero:#252525;
  --panel:#2b2b2b;
  --box:#232323;
  --footer:#242424;
  --text:#ffffff;
  --muted:#e4e4e4;
  --line:#444444;
  --green:#3fae49;
}
*{margin:0;padding:0;box-sizing:border-box}
html,body{width:1162px;height:1200px;overflow:hidden}
body{position:relative;font-family:'Lato',sans-serif;color:var(--text);background:var(--footer)}
.abs{position:absolute}
.band{position:absolute;left:0;width:1162px}
.topbar{top:0;height:30px;background:var(--bar);font-size:10px}
.header{top:30px;height:159px;background:var(--header)}
.hero{top:189px;height:231px;background:var(--hero)}
.order{top:420px;height:456px;background:var(--panel)}
.footer{top:876px;height:324px;background:var(--footer)}
.brand{font-weight:900;font-size:24px;letter-spacing:1px;text-transform:uppercase;display:flex;align-items:center;gap:7px;transform:translateX(-50%)}
.brand .dot{width:10px;height:10px;background:var(--text)}
.nav{top:158px;left:0;width:1162px;display:flex;justify-content:center;gap:0;font-size:11.5px;letter-spacing:1px}
.nav span{display:inline-flex;align-items:center;gap:6px;padding:0 16px}
.center{left:0;width:1162px;text-align:center}
.label{font-weight:700;font-size:13px}
.val{font-size:11px;color:var(--muted);letter-spacing:.4px}
.photo{width:71px;height:94px;background:linear-gradient(135deg,#f4f4f2 0%,#f0f0ec 40%,#c98a1c 55%,#6aa53a 75%,#f2f2ef 100%)}
.rule{height:1px;background:var(--line)}
.sumline{font-size:11px;color:var(--muted);line-height:17.5px}
.foottext{font-size:10px;line-height:23.5px;text-align:center}
</style>
</head>
<body>
<div class="band topbar">
  <span class="abs" style="left:84px;top:9px">Welcome to Our store Vale Ember</span>
  <span class="abs" style="left:240px;top:9px;display:flex;gap:6px;align-items:center">
    <svg width="8" height="8" viewBox="0 0 10 10"><path d="M2 0l2 2.5-1.2 1.3a6 6 0 0 0 3.4 3.4L7.5 6 10 8l-1 2C4 10 0 6 0 1z" fill="#fff"/></svg>Call Us: 123 - 456 - 7890</span>
  <span class="abs" style="left:903px;top:9px;color:#ccc">&#9829; Wishlist</span>
  <span class="abs" style="left:993px;top:9px">&#9679; My Account &#8964;</span>
</div>

<div class="band header">
  <svg class="abs" style="left:84px;top:48px" width="18" height="15"><rect y="0" width="18" height="2.5" fill="#fff"/><rect y="6" width="18" height="2.5" fill="#fff"/><rect y="12" width="18" height="2.5" fill="#fff"/></svg>
  <div class="abs brand" style="left:581px;top:42px"><span class="dot"></span>Vale Ember</div>
  <svg class="abs" style="left:993px;top:47px" width="18" height="18" fill="none" stroke="#fff" stroke-width="1.6"><circle cx="7.5" cy="7.5" r="6"/><path d="M12 12l5 5"/></svg>
  <svg class="abs" style="left:1027px;top:47px" width="18" height="18" fill="none" stroke="#fff" stroke-width="1.4"><circle cx="9" cy="9" r="3"/><circle cx="9" cy="9" r="7" stroke-dasharray="3 1.5"/></svg>
  <svg class="abs" style="left:1061px;top:47px" width="18" height="18" fill="none" stroke="#fff" stroke-width="1.4"><path d="M1 7h16l-2 9H3z M5 7l4-5 4 5 M7 10v4 M11 10v4"/></svg>
  <div class="abs rule" style="left:84px;top:112px;width:994px"></div>
</div>
<div class="abs nav">
  <span>HOME</span><span>SHOP &#8964;</span><span>ABOUT</span><span>PRODUCT &#8964;</span><span>BRANDS &#8964;</span><span>BLOG</span><span>FAQ</span>
</div>

<div class="band hero">
  <svg class="abs" style="left:566px;top:54px" width="30" height="30"><circle cx="15" cy="15" r="15" fill="var(--green)"/><path d="M8 15.5l5 5 9-10" stroke="#222" stroke-width="3.5" fill="none"/></svg>
  <div class="abs center" style="top:92px;font-size:26px;font-weight:700">THANK YOU</div>
  <div class="abs center" style="top:130px;font-size:13px">Payment Is Successfully Processsed And Your Order Is On The Way</div>
  <div class="abs center" style="top:154px;font-size:13px">Transaction ID:507676GGDTT275467</div>
</div>

<div class="band order">
  <div class="abs" style="left:84px;top:51px;font-size:17.5px;font-weight:700">YOUR ORDER DETAILS</div>
  <div class="abs photo" role="img" aria-label="Product photo: amber oil dropper bottle beside a green leaf" style="left:84px;top:82px"></div>
  <div class="abs label" style="left:211px;top:112px">Product Name</div><div class="abs val" style="left:211px;top:132px">Cannabis Product</div>
  <div class="abs label" style="left:338px;top:112px">Quantity</div><div class="abs val" style="left:338px;top:132px">1</div>
  <div class="abs label" style="left:465px;top:112px">Price</div><div class="abs val" style="left:465px;top:132px">$350.00</div>
  <div class="abs photo" role="img" aria-label="Product photo: amber oil dropper bottle beside a green leaf" style="left:84px;top:188px"></div>
  <div class="abs label" style="left:211px;top:218px">Product Name</div><div class="abs val" style="left:211px;top:238px">Cannabis Product</div>
  <div class="abs label" style="left:338px;top:218px">Quantity</div><div class="abs val" style="left:338px;top:238px">1</div>
  <div class="abs label" style="left:465px;top:218px">Price</div><div class="abs val" style="left:465px;top:238px">$256.00</div>
  <div class="abs rule" style="left:84px;top:293px;width:486px"></div>
  <div class="abs" style="left:84px;top:306px;width:486px;font-size:13px;line-height:19.5px;display:grid;grid-template-columns:1fr auto">
    <span>Subtotal</span><span>$30.00</span><span>Shipping</span><span>$50.00</span><span>Tax(GST)</span><span>$61.00</span>
  </div>
  <div class="abs rule" style="left:84px;top:374px;width:486px"></div>
  <div class="abs" style="left:84px;top:385px;width:486px;display:flex;justify-content:space-between;font-size:18px;font-weight:700"><span>TOTAL</span><span>$156.00</span></div>

  <div class="abs label" style="left:592px;top:50px">Summery</div>
  <div class="abs sumline" style="left:592px;top:70px">Order ID: 3586133658932<br>Order Date: September 30, 2020<br>Order Total: $907.28</div>
  <div class="abs label" style="left:846px;top:50px">Shipping Address</div>
  <div class="abs sumline" style="left:846px;top:70px">Lorem Ipsum Dolor<br>120, Suite Ave.<br>India, 235153<br>Contact No. 1234567890</div>
  <div class="abs label" style="left:592px;top:138px">Payment Method</div>
  <div class="abs" style="left:592px;top:159px;width:486px;font-size:11px;line-height:14.5px;color:var(--muted)">Pay on Delivery (Cash/Card). Cash on delivery (COD) available. Card/Net banking acceptance subject to device availability.</div>
  <div class="abs" style="left:592px;top:202px;width:486px;height:101px;background:var(--box);text-align:center">
    <div style="margin-top:21px;font-size:17.5px;letter-spacing:.5px">Expected Date Of Delivery</div>
    <div style="margin-top:3px;font-size:26px;font-weight:700">September 30, 2020</div>
  </div>
</div>

<div class="band footer">
  <div class="abs brand" style="left:200px;top:68px"><span class="dot"></span>Vale Ember</div>
  <div class="abs foottext" style="left:74px;width:252px;top:126px">Lorem ipsum dolor sit amet, consectetur adipiscing elit, sed do eiusmod tempor incididunt ut labore et.Lorem ipsum dolor sit amet, consectetur adipiscing</div>
  <div class="abs" style="left:338px;top:51px;width:1px;height:141px;background:var(--line)"></div>
  <div class="abs" style="left:823px;top:51px;width:1px;height:141px;background:var(--line)"></div>
  <div class="abs" style="left:338px;width:485px;top:57px;text-align:center;font-size:26px;font-weight:700">NEWSLETTER</div>
  <div class="abs" style="left:418px;top:107px;width:325px;height:36px;border:1px solid #3a3a3a;background:#272727;text-align:center;line-height:34px;font-size:8.5px;letter-spacing:3px;color:#aaa">Enter your email</div>
  <div class="abs" style="left:530px;top:151px;width:102px;height:34px;border:1px solid #fff;text-align:center;line-height:32px;font-size:10px;font-weight:700;letter-spacing:.5px">SUBSCRIBE</div>
  <div class="abs" style="left:870px;width:183px;top:58px;text-align:center;font-size:13.5px;font-weight:700">STORE INFORMATION</div>
  <div class="abs" style="left:870px;width:183px;top:84px;text-align:center;font-size:10px;line-height:21.8px">Vale Ember Store, Demo store<br>USA 123-456<br>Call Us: 123-456-7890<br>Email Us: info@example.com<br>Fax: 123456</div>
  <div class="abs rule" style="left:73px;top:270px;width:1016px"></div>
  <div class="abs" style="left:84px;top:290px;font-size:10px">&copy; 2020 All Right Reserved</div>
  <div class="abs" style="left:930px;top:289px;display:flex;gap:12px" role="img" aria-label="Accepted payment methods">
    <span style="width:19px;height:19px;border-radius:50%;background:#f2f2f2"></span>
    <span style="width:19px;height:19px;border-radius:50%;background:#3f78b5"></span>
    <span style="width:19px;height:19px;border-radius:50%;background:#f2f2f2"></span>
    <span style="width:19px;height:19px;border-radius:50%;background:#2fa3dc"></span>
    <span style="width:19px;height:19px;border-radius:50%;background:#f2f2f2"></span>
  </div>
</div>
</body>
</html>
```